Business Card Design needed for logo design project

Would like a professional business card for a company involved in financial and latest technologies including CAD design. We would like the card to convey professionalism and communicate that we are involved in up to date technology solutions.

Target Market(s)

Business 2 Business sales

Industry/Entity Type

Financial

Colors

Designer to choose colors to be used in the design.

Requirements
Must have
• Business Name
Logo
Name
Phone
Email
Nice to have
• Website

```html
<!DOCTYPE html>
<html lang="en">
<head>
<meta charset="utf-8">
<title>Novaris Business Cards</title>
<link rel="stylesheet" href="https://fonts.googleapis.com/css2?family=Exo+2:ital,wght@0,300;0,400;0,600;1,300;1,400&display=swap">
<style>
  :root {
    --backdrop: #e6e6e6;
    --card-white: #f7f7f6;
    --brand-red: #c8242b;
    --accent-red: #d2412f;
    --brand-navy: #29325f;
    --name-tint: #c9ccd8;
    --body-grey: #4a4a4a;
    --pure-white: #ffffff;
  }
  * { margin: 0; padding: 0; box-sizing: border-box; }
  html, body {
    width: 1200px;
    height: 1000px;
    overflow: hidden;
    background: var(--backdrop);
    font-family: "Exo 2", sans-serif;
  }
  .card-set {
    position: absolute;
    top: 343px;
    left: 80px;
    display: flex;
    gap: 60px;
  }
  .card {
    width: 490px;
    height: 315px;
    display: block;
    box-shadow: 0 3px 10px rgba(0,0,0,0.12);
  }
  .wordmark { font-family: "Exo 2", sans-serif; font-weight: 600; letter-spacing: 1px; }
  .person-name { font-family: "Exo 2", sans-serif; font-weight: 300; }
  .person-title { font-family: "Exo 2", sans-serif; font-weight: 300; font-style: italic; }
  .contact-label { font-family: "Exo 2", sans-serif; font-weight: 400; font-style: italic; }
  .contact-value { font-family: "Exo 2", sans-serif; font-weight: 400; }
</style>
</head>
<body>
  <main class="card-set">
    <svg class="card card-front" viewBox="0 0 350 225" aria-label="Card front">
      <rect width="350" height="225" fill="var(--brand-red)"/>
      <polygon class="corner-wedge" points="0,0 113,0 0,155" fill="var(--pure-white)"/>
      <polygon class="corner-band" points="0,22 62,22 0,108" fill="var(--brand-red)"/>
      <text class="wordmark" x="320" y="196" text-anchor="end" font-size="17" fill="var(--pure-white)">NOVARIS</text>
    </svg>

    <svg class="card card-back" viewBox="0 0 350 225" aria-label="Card back">
      <rect width="350" height="225" fill="var(--card-white)"/>
      <text class="wordmark" x="325" y="39" text-anchor="end" font-size="17" fill="var(--brand-red)">NOVARIS</text>

      <polygon class="navy-band" points="0,72 252,72 135,225 80,225 117,140 0,140" fill="var(--brand-navy)"/>
      <polygon class="red-block" points="0,176 60,176 40,225 0,225" fill="var(--accent-red)"/>

      <text class="person-name" x="70" y="111" font-size="15" fill="var(--name-tint)">Daniel Reyes</text>
      <text class="person-title" x="70" y="127" font-size="8.5" fill="var(--name-tint)">Managing Director</text>

      <g class="contact-list" font-size="7.5" text-anchor="end">
        <text x="327" y="180"><tspan class="contact-label" fill="var(--brand-red)">Phone: </tspan><tspan class="contact-value" fill="var(--body-grey)">555-987-210</tspan></text>
        <text x="327" y="191"><tspan class="contact-label" fill="var(--brand-red)">Email: </tspan><tspan class="contact-value" fill="var(--body-grey)">contact@novaris.com</tspan></text>
        <text x="327" y="202"><tspan class="contact-label" fill="var(--brand-red)">Web: </tspan><tspan class="contact-value" fill="var(--body-grey)">www.novaris.com</tspan></text>
      </g>
    </svg>
  </main>
</body>
</html>
```